Harbourlight Geriatric care need Business card design

Simple and elegance looking business card (colour choice will be very important)
Harbourlight geriatric care is medical consultation service for elderly population.

1st side---business logo and the doctor name/tile
eg: dr. XXX
MBBS,FRACP etc
Main room:
suite xxx AAA medical centre 18 XXX road Vic 3000
Phone:
Fax:

2nd side --different clinic address (up to 3 addresses) and need to have appointment time/ date

Suite xxx AAA medical centre , 18 XXX road VIC 3000

Please see attachment for business logo

Important: need to be compatible with Quillo Press for printing purpose.

Thank you.

hi, please look at the sample business card and create something similar. Company name: Harbourlight Geriatric Care PTY LTD ABN 47580916 ( all small font and no need to be obvious) company logo need to be obvious Apart from steadfast in support, also add Geriatrician for Community and Residential Care. Main room Pondaro Medical Centre suite 2.07 204-206 Larkspur street Box Hill Vic All appointment and enquiries: tel: 908716252 Fasmile: www.qwvplmzk.com.au Tindlewood Medical Centre 42 gorrington road mooroolbark VIC Bayview Crest Private Frankston 87 Pellworth road , franskton VIC 3199 Oakrun Private Hospital specialist room 259 Dunmore Road, Mt. Waverley VIC 3333 Dr. TM 81920kp DR. RH w7169208nd DR. PJ 670918vt Thank you

```html
<!DOCTYPE html>
<html lang="en">
<head>
<meta charset="utf-8">
<title>Harbourlight Geriatric Care – Business Card</title>
<link href="https://fonts.googleapis.com/css2?family=Arimo:wght@400;700&display=swap" rel="stylesheet">
<style>
  :root {
    --navy: #2b4592;
    --navy-dark: #1f3475;
    --red: #d8303f;
    --white: #ffffff;
    --paper: #f6f6f6;
    --grey: #7d7f86;
    --stage: #e4e4e6;
  }
  * { margin: 0; padding: 0; box-sizing: border-box; }
  html, body { width: 1200px; height: 885px; overflow: hidden; background: var(--stage); }
  body { font-family: "Arimo", Arial, sans-serif; position: relative; }

  .card {
    position: absolute;
    width: 525px; height: 300px;
    top: 292px;
    background: var(--paper);
    box-shadow: 0 6px 18px rgba(0,0,0,.18);
    overflow: hidden;
  }
  .card--front { left: 45px; }
  .card--back { left: 630px; }
  .card__art { position: absolute; inset: 0; }

  .brand { position: absolute; display: flex; align-items: center; gap: 10px; }
  .brand__dot { width: 30px; height: 30px; border-radius: 50%; background: var(--red); flex: none; }
  .brand__name { font-weight: 700; font-size: 23px; color: var(--navy); white-space: nowrap; }
  .brand__tagline {
    position: absolute; font-size: 9.5px; letter-spacing: 5px;
    color: var(--grey); text-transform: uppercase; white-space: nowrap;
  }

  .card--front .brand { left: 28px; top: 36px; }
  .card--front .brand__tagline { left: 70px; top: 76px; }

  .person { position: absolute; left: 40px; top: 196px; }
  .person__name { font-size: 21px; font-weight: 700; color: var(--red); white-space: nowrap; }
  .person__title { font-size: 13px; color: var(--grey); margin-top: 5px; }

  .contact { position: absolute; left: 368px; top: 108px; color: var(--white); font-size: 11.5px; line-height: 1.6; white-space: nowrap; }
  .contact__row { display: flex; align-items: center; gap: 7px; padding-left: 22px; }
  .contact__row svg { width: 11px; height: 11px; flex: none; }
  .contact__address { margin-top: 18px; }

  .card--back .brand { left: 36px; top: 34px; }
  .card--back .brand__tagline { left: 78px; top: 74px; }
  .appointment { position: absolute; left: 36px; top: 112px; color: var(--navy); font-size: 13px; width: 330px; }
  .appointment__row { display: flex; align-items: flex-end; gap: 6px; margin-bottom: 8px; }
  .appointment__line { flex: 1; border-bottom: 1px solid var(--navy-dark); height: 12px; }
  .clinics { position: absolute; left: 36px; top: 196px; color: var(--navy); font-size: 12.5px; line-height: 1.7; white-space: nowrap; }
</style>
</head>
<body>

<section class="card card--front" aria-label="Business card front">
  <svg class="card__art" viewBox="0 0 525 300" aria-hidden="true">
    <rect width="525" height="300" fill="#f6f6f6"/>
    <path d="M225 300 C 290 250, 300 180, 292 120" fill="none" stroke="#d8303f" stroke-width="7" stroke-linecap="round"/>
    <path d="M248 300 C 320 240, 330 170, 312 100" fill="none" stroke="#2b4592" stroke-width="9" stroke-linecap="round"/>
    <path d="M265 300 C 340 250, 360 150, 420 0 L525 0 L525 300 Z" fill="#2b4592"/>
  </svg>

  <div class="brand">
    <span class="brand__dot"></span>
    <span class="brand__name">Harbourlight Geriatric Care</span>
  </div>
  <div class="brand__tagline">Steadfast in support</div>

  <div class="person">
    <div class="person__name">Employee Name</div>
    <div class="person__title">MBBS,FRACP</div>
  </div>

  <div class="contact">
    <div class="contact__row">
      <svg viewBox="0 0 12 12"><path d="M2 1 L4.5 1 L5.5 3.5 L4 4.6 C4.6 6 6 7.4 7.4 8 L8.5 6.5 L11 7.5 L11 10 C11 10.6 10.6 11 10 11 C5 11 1 7 1 2 C1 1.4 1.4 1 2 1 Z" fill="#fff"/></svg>
      <span>xxxx xxx xxx</span>
    </div>
    <div class="contact__row">
      <svg viewBox="0 0 12 12"><rect x="1" y="4" width="10" height="6" rx="1" fill="#fff"/><rect x="3" y="1" width="6" height="3" fill="#fff"/></svg>
      <span>xxxx xxx xxx</span>
    </div>
    <div class="contact__address">
      suite xxx AAA medical centre<br>
      18 XXX road Vic 3000
    </div>
  </div>
</section>

<section class="card card--back" aria-label="Business card back">
  <svg class="card__art" viewBox="0 0 525 300" aria-hidden="true">
    <rect width="525" height="300" fill="#2b4592"/>
    <path d="M0 0 L330 0 C 470 40, 520 190, 455 300 L0 300 Z" fill="#d8303f"/>
    <path d="M0 0 L318 0 C 455 45, 505 190, 442 300 L0 300 Z" fill="#f6f6f6"/>
  </svg>

  <div class="brand">
    <span class="brand__dot"></span>
    <span class="brand__name">Harbourlight Geriatric Care</span>
  </div>
  <div class="brand__tagline">Steadfast in support</div>

  <div class="appointment">
    <div class="appointment__row"><span>Appointment</span><span class="appointment__line"></span></div>
    <div class="appointment__row"><span>Date:</span><span class="appointment__line"></span><span>Time:</span><span class="appointment__line"></span></div>
  </div>

  <div class="clinics">
    Suite xxx AAA medical centre , 18 XXX road VIC 3000<br>
    Suite xxx AAA medical centre , 18 XXX road VIC 3000<br>
    Suite xxx AAA medical centre , 18 XXX road VIC 3000
  </div>
</section>

</body>
</html>
```